Virtual Reality company needs business card design

We would like a business card that is simple and memorable. Telvani is a global startup based in San Francisco and Singapore. We are a company with products and services for both the B2B and B2C audiences. We develop platforms with educational content, and allow people to interact with the content in a virtual environment setting. Our end user will be able to learn and 'see' the world's culture and history from the comfort of their home. The business card will primarily be used for B2B audience and not overly corporate in image, but requires a universal appeal - evoking sense of friendliness and innovation. Attached is our logo with two color options. We are open to single-sided or double-sided designs. EPS/AI files will be provided to winning designer at final design stage.

Other text that will be included in card: (Name), (Address), (Tel), (Email), (Website)

Include option of having TWO QR codes which are 0.5 inch x 0.5 inch each
Updates

Dear Designers,

Thank you for your submissions. We are currently in process of reviewing your designs and will make a decision in the next few days.

Regards,
Telvani

Industry/Entity Type

Environment

Font styles to use
Serif
Sans Serif

Requirements
Must have
• Spacing for Name, Address, Tel, Email, Web address
Should not have
• Limit the number of colors utilised.

```html
<!DOCTYPE html>
<html lang="en">
<head>
<meta charset="utf-8">
<title>Telvani business card</title>
<link href="https://fonts.googleapis.com/css2?family=Open+Sans:wght@400;600;700&display=swap" rel="stylesheet">
<style>
  :root {
    --teal: #5bbcc8;
    --teal-soft: #a9dde3;
    --teal-text: #3fb3c2;
    --ink: #555a5e;
    --paper: #ffffff;
    --backdrop: #e6e6e6;
  }
  * { margin: 0; padding: 0; box-sizing: border-box; }
  html, body {
    width: 1200px;
    height: 900px;
    overflow: hidden;
    background: var(--backdrop);
    font-family: "Open Sans", Arial, sans-serif;
  }
  .canvas {
    position: relative;
    width: 1200px;
    height: 900px;
  }
  .card {
    position: absolute;
    width: 525px;
    height: 300px;
    overflow: hidden;
    box-shadow: 0 10px 28px rgba(0, 0, 0, 0.12);
  }
  .card-front {
    left: 575px;
    top: 95px;
    background: var(--teal);
  }
  .card-back {
    left: 100px;
    top: 505px;
    background: var(--paper);
  }
  .edge-band {
    position: absolute;
    left: 0;
    top: 0;
    width: 70px;
    height: 100%;
  }
  .card-front .edge-band { background: rgba(255, 255, 255, 0.28); }
  .card-back .edge-band { background: var(--teal-soft); }
  .brand {
    position: absolute;
    left: 175px;
    top: 112px;
    display: flex;
    align-items: center;
    gap: 14px;
    color: var(--paper);
  }
  .brand-name {
    font-size: 54px;
    font-weight: 400;
    letter-spacing: 1px;
    line-height: 1;
  }
  .brand-dot {
    width: 22px;
    height: 22px;
    border-radius: 50%;
    background: var(--paper);
  }
  .contact {
    position: absolute;
    right: 40px;
    top: 78px;
    text-align: right;
    color: var(--ink);
    font-size: 15px;
    line-height: 1.35;
  }
  .contact-name {
    font-size: 19px;
    font-weight: 700;
  }
  .contact-role {
    font-size: 16px;
    font-weight: 600;
    color: var(--teal-text);
    margin-bottom: 4px;
  }
  .contact-line {
    display: flex;
    justify-content: flex-end;
    align-items: center;
    gap: 6px;
  }
  .contact-key {
    width: 20px;
    height: 20px;
    border: 2px solid var(--teal-text);
    border-radius: 50%;
    color: var(--teal-text);
    font-size: 12px;
    font-weight: 700;
    line-height: 16px;
    text-align: center;
  }
  .contact-address { margin-top: 8px; }
</style>
</head>
<body>
<main class="canvas">
  <section class="card card-front" aria-label="Card front">
    <div class="edge-band"></div>
    <div class="brand">
      <span class="brand-name">Telvani</span>
      <span class="brand-dot"></span>
    </div>
  </section>

  <section class="card card-back" aria-label="Card back">
    <div class="edge-band"></div>
    <div class="contact">
      <p class="contact-name">Your Name</p>
      <p class="contact-role">Managing Director</p>
      <p class="contact-line">0123 456 789 <span class="contact-key">t</span></p>
      <p class="contact-line">your.name@telvani.com <span class="contact-key">e</span></p>
      <p class="contact-address">Address Line One<br>Address Line Two,&nbsp; ZIP CODE</p>
    </div>
  </section>
</main>
</body>
</html>
```